Neue Marke für Herrenaccessoires benötigt Flyer-Design
Zielgruppe
Wir sind ein junges Unternehmen die eine neue Marke für Herrenaccessoires aufbaut. KORVALO ist unsere neue Marke für hochwertige, stylishe Herrenaccessoires. Entstanden ist die Idee bie der Suche nach dem kompletten Look für den modernen Gentleman. Warum darf es bei den Herrenaccessoires nicht etwas mutiger zugehen in Sachen Farben und Mustern und das mit dem Anspruch hoher Materialqualität und Verarbeitung? Wo findet man komplette Accessoires-Angebote, bei denen man Krawatten, Einstecktücher, Socken, Gürtel und sogar Taschen in einem Shop farblich aufeinander abgestimmt finden kann? Diese Fragen haben wir uns gestellt und geben mit KORVALO unsere Antwort darauf. Mit KORVALO finden unsere Kunden sowohl für ihren Business- als auch für ihren Freizeitlook in Farbe und Styles perfekt kombinierbare Accessoires, die wir in von uns persönlich ausgewählten Manufakturen in Italien und der Türkei mit Sorgfalt und Know-how fertigen lassen.
Vom kontrastreichen, mutigen trendy Muster- und Farbmix zur klassischen Kombination Ton in Ton mit aktuellen Farben.
Unsere Zielgruppen sind mode- und stilbewusste Herren im Alter von 30 - 50.
Aufgabenstellung
Das Design sollte sich an unserem Web-Shop www.korvalo-shop.example orientieren.
Die Market KORVALO clean, minimalistisch und edel wahrgenommen werden.
Wir möchten die erste Marketingkampage mit einem Flyer starten. Die Flyer werden über eine Textilreinigungsfirma an die Reinigungsbügel (bei Hemden) befestigt. Aus diesem Grund sollte das Layout die Maße von ca. Breite: 9,5 cm x Höhe: 20 cm orientieren. Damit der Flyer (2seitig) auch an die Bügel umgehängt werden kann, muss oben auf dem Flyer ein Loch mit einem Durchmesser von 3 cm ein berücksichtigt werden.

```html
<!DOCTYPE html>
<html lang="de">
<head>
<meta charset="utf-8">
<title>KORVALO – Bügelanhänger</title>
<link href="https://fonts.googleapis.com/css2?family=Montserrat:wght@700&family=Questrial&display=swap" rel="stylesheet">
<style>
  :root {
    --paper: #ffffff;
    --stage: #ffffff;
    --ink: #111111;
    --band: #000000;
    --on-band: #ffffff;
    --hole-edge: #a9a9a9;
    --muted: #222222;
    --mark-a: #2f3b57;
    --mark-b: #6a3a4a;
  }
  * { margin: 0; padding: 0; box-sizing: border-box; }
  html, body { width: 1200px; height: 1015px; overflow: hidden; background: var(--stage); }
  body { position: relative; font-family: "Questrial", sans-serif; color: var(--ink); }

  .hanger {
    position: absolute; top: 204px; width: 318px; height: 679px;
    background: var(--paper); overflow: hidden;
    box-shadow: 0 2px 10px rgba(0,0,0,.22);
  }
  .hanger--front { left: 213px; }
  .hanger--back { left: 610px; }

  .hanger__hole {
    position: absolute; left: 109px; top: 16px; width: 100px; height: 100px;
    border-radius: 50%; border: 2px solid var(--hole-edge); background: var(--stage);
    box-shadow: inset 0 -4px 8px rgba(0,0,0,.12);
  }

  .block { position: absolute; left: 0; width: 100%; }
  .band { background: var(--band); color: var(--on-band); text-align: center; }

  /* Front */
  .hero-photo {
    position: absolute; left: 0; top: 122px; width: 196px; height: 346px;
    background: radial-gradient(ellipse 45% 75% at 42% 58%, #4a4a4a 0%, #777 45%, #c9c9c9 75%, rgba(255,255,255,0) 100%),
                linear-gradient(90deg, #e4e4e4 0%, #f4f4f4 70%, #ffffff 100%);
  }
  .brand-name {
    position: absolute; left: 174px; width: 120px; top: 205px; text-align: center;
    font-size: 18px; letter-spacing: 3px; color: var(--ink);
  }
  .headline {
    position: absolute; left: 173px; width: 122px; top: 278px;
    text-align: center; font-size: 19px; font-weight: 400; line-height: 22px; letter-spacing: .5px;
  }
  .categories {
    top: 468px; height: 42px; line-height: 42px;
    font-family: "Montserrat", sans-serif; font-weight: 700; font-size: 11px;
    word-spacing: 3px;
  }
  .accessory-strip {
    top: 510px; height: 78px;
    background: linear-gradient(90deg, #9ea348 0%, #b9bb6a 22%, #8a8a8a 45%, #3e3f46 68%, #34363f 100%);
  }
  .shop-info { top: 588px; height: 91px; padding-top: 4px; font-size: 14px; line-height: 17px; }
  .shop-info__url { margin-bottom: 7px; }

  /* Back */
  .outfit-photo {
    top: 142px; height: 208px;
    background: radial-gradient(ellipse 40% 70% at 28% 50%, #8c8c8c 0%, #555 55%, rgba(30,30,30,0) 100%),
                radial-gradient(ellipse 25% 30% at 70% 70%, #6b5646 0%, rgba(30,30,30,0) 100%),
                #1e1e1e;
  }
  .offer {
    position: absolute; left: 167px; top: 159px; width: 150px;
    color: var(--on-band); font-size: 14.5px; line-height: 17px;
  }
  .code { top: 350px; height: 47px; line-height: 47px; font-size: 14.5px; }
  .scarf-photo {
    top: 397px; height: 113px;
    background: linear-gradient(100deg, #e6dfcc 0%, #c9c2ae 20%, #3366a8 40%, #a67f2e 65%, #7e2a3a 85%, #241e20 100%);
  }
  .social-call { top: 510px; height: 50px; padding-top: 7px; font-size: 14.5px; line-height: 18px; }

  .social {
    position: absolute; top: 580px; left: 0; width: 100%;
    display: flex; justify-content: center; gap: 22px;
  }
  .social__item { display: flex; flex-direction: column; align-items: center; font-size: 11px; color: var(--muted); }
  .social__mark { width: 24px; height: 24px; border-radius: 50%; margin-bottom: 7px; }
  .social__mark--a { background: var(--mark-a); }
  .social__mark--b { background: var(--mark-b); }

  .footnote {
    position: absolute; top: 643px; left: 0; width: 100%;
    text-align: center; font-size: 10px; line-height: 13px; color: var(--muted);
  }
</style>
</head>
<body>

<section class="hanger hanger--front" aria-label="Vorderseite">
  <div class="hanger__hole"></div>
  <div class="hero-photo" role="img" aria-label="Schwarzweißfoto eines Mannes im Anzug mit verschränkten Armen an einer Wand"></div>
  <div class="brand-name">KORVALO</div>
  <h1 class="headline">Lust auf einen neuen Style?</h1>
  <div class="block band categories">Krawatten Einstecktücher Socken Gürtel Taschen</div>
  <div class="block accessory-strip" role="img" aria-label="Nahaufnahme von Krawatte, Sakkostoff und Einstecktuch"></div>
  <div class="block band shop-info">
    <p class="shop-info__url">Lass Dich inspirieren: www.korvalo-shop.example</p>
    <p>Der neue Online-Shop mit hochwertigen,<br>stylishen Herrenaccessoires für den<br>modernen Gentleman.</p>
  </div>
</section>

<section class="hanger hanger--back" aria-label="Rückseite">
  <div class="hanger__hole"></div>
  <div class="block outfit-photo" role="img" aria-label="Gemustertes Sakko, Ledertasche und Accessoires vor dunklem Hintergrund"></div>
  <p class="offer">Sicher Dir jetzt<br>sich jetzt 20 % Rabatt<br>auf unsere Artikel!</p>
  <div class="block band code">Ihr 20% Rabattcode*: Blankexxx</div>
  <div class="block scarf-photo" role="img" aria-label="Gefaltete Einstecktücher in Creme, Blau, Gold und Rot"></div>
  <div class="block band social-call">Besuche uns auch<br>auf Facenet und Pictagram!</div>
  <div class="social">
    <div class="social__item"><span class="social__mark social__mark--a"></span>KORVALO</div>
    <div class="social__item"><span class="social__mark social__mark--b"></span>korvalo-official</div>
  </div>
  <p class="footnote">*Gültig bis zum xx.xx.xxxx,<br>nicht kombinierbar mit anderen Rabattaktionen.</p>
</section>

</body>
</html>
```